Redesign of iOS App Lumo Tutor

Redesign of existing App Lumo Tutor, an app that helps learning Japanese Kanjis, Hiragana, Katakana.

The functionallity should remain the same as today: the app is free, you may download it at the app store. But: I like the design of my other apps better ;)

Target Market(s)

Students learning Japanese

Industry/Entity Type

Teacher

Font styles to use
Sans Serif

Requirements
Must have
• Lumo Tutor has 7 main screens, all screens has to be designed for iPhone and iPad: Main, Settings, Reading Tests, Writing Tests, Game, Paper Mode, Search
Nice to have
• I like the logo as it is today

```html
<!DOCTYPE html>
<html lang="en">
<head>
<meta charset="utf-8">
<title>Lumo Tutor – Reading Test</title>
<link rel="stylesheet" href="https://fonts.googleapis.com/css2?family=Montserrat:wght@300;400;500;600;700&family=Noto+Sans+JP:wght@400;500;700&display=swap">
<style>
  :root {
    --brand-red: #bc1a2c;
    --header-label: #f2808a;
    --back-arrow: #f0727a;
    --white: #ffffff;
    --ink: #000000;
    --reading-grey: #cccccc;
    --option-text: #9b9b9b;
    --option-border: #e2e2e2;
    --wrong: #f26c5e;
    --correct: #2ecc71;
    --favorite: #f5a623;
    --favorite-star: #f8d48a;
    --skip: #3a8fd9;
  }
  * { box-sizing: border-box; margin: 0; padding: 0; }
  html, body {
    width: 675px; height: 1200px; overflow: hidden;
    background: var(--white);
    font-family: "Montserrat", "Helvetica Neue", Arial, sans-serif;
  }
  .screen { position: relative; width: 675px; height: 1200px; overflow: hidden; background: var(--white); }

  .app-header { position: absolute; left: 0; top: 0; width: 675px; height: 162px; background: var(--brand-red); color: var(--white); }
  .status-bar { position: absolute; top: 12px; left: 0; width: 100%; height: 26px; font-size: 19px; font-weight: 400; }
  .status-carrier { position: absolute; left: 23px; top: 0; display: flex; align-items: center; gap: 6px; }
  .status-time { position: absolute; left: 0; right: 0; text-align: center; font-weight: 500; }
  .status-battery { position: absolute; right: 22px; top: 4px; }

  .back-button { position: absolute; left: 32px; top: 86px; }

  .score { position: absolute; top: 64px; width: 160px; text-align: center; }
  .score-value { display: block; font-size: 48px; font-weight: 300; line-height: 1; letter-spacing: -0.5px; }
  .score-label { display: block; margin-top: 9px; font-size: 11.5px; font-weight: 400; color: var(--header-label); letter-spacing: 0.2px; }
  .score-remaining { left: 142px; }
  .score-correct { left: 325px; }
  .score-wrong { left: 489px; }

  .kanji { position: absolute; top: 198px; left: 0; width: 100%; text-align: center; font-family: "Noto Sans JP", sans-serif; font-size: 118px; font-weight: 700; color: var(--ink); line-height: 1.2; }
  .reading { position: absolute; top: 345px; left: 0; width: 100%; text-align: center; font-family: "Noto Sans JP", sans-serif; font-size: 33px; font-weight: 500; color: var(--reading-grey); }

  .answer-grid {
    position: absolute; left: 20px; top: 447px;
    display: grid; grid-template-columns: 196px 187px 196px; grid-auto-rows: 160px;
    column-gap: 28px; row-gap: 24.5px;
  }
  .answer {
    display: flex; align-items: center; justify-content: center;
    border: 1px solid var(--option-border); border-radius: 6px; background: var(--white);
    font-size: 21.5px; font-weight: 500; color: var(--option-text); letter-spacing: 0.3px;
  }
  .answer.is-wrong { border: 2px solid var(--wrong); color: var(--wrong); box-shadow: 0 3px 10px rgba(242,108,94,0.3); }
  .answer.is-correct { border: 2px solid var(--correct); color: var(--correct); box-shadow: 0 3px 10px rgba(46,204,113,0.3); }

  .action { position: absolute; top: 1044px; height: 67px; border-radius: 6px; background: var(--white);
    display: flex; align-items: center; justify-content: center; gap: 12px;
    font-size: 19px; font-weight: 700; letter-spacing: 0.2px; text-transform: uppercase; }
  .action-favorite { left: 20px; width: 344px; border: 2px solid var(--favorite); color: var(--favorite); }
  .action-skip { left: 383px; width: 273px; border: 2px solid var(--skip); color: var(--skip); }
</style>
</head>
<body>
<main class="screen">
  <header class="app-header">
    <div class="status-bar">
      <span class="status-carrier">Carrier
        <svg width="20" height="15" viewBox="0 0 20 15" aria-hidden="true">
          <path d="M10 14 L7 10.5 A4.5 4.5 0 0 1 13 10.5 Z" fill="#fff"/>
          <path d="M3.5 7.2 A9 9 0 0 1 16.5 7.2" stroke="#fff" stroke-width="2" fill="none" stroke-linecap="round"/>
          <path d="M1 4 A13 13 0 0 1 19 4" stroke="#fff" stroke-width="2" fill="none" stroke-linecap="round"/>
        </svg>
      </span>
      <span class="status-time">1:23 PM</span>
      <svg class="status-battery" width="42" height="18" viewBox="0 0 42 18" aria-hidden="true">
        <rect x="1" y="1" width="36" height="16" rx="3" fill="none" stroke="#fff" stroke-width="1.5"/>
        <rect x="3" y="3" width="32" height="12" rx="1.5" fill="#fff"/>
        <rect x="38.5" y="6" width="2.5" height="6" rx="1" fill="#fff"/>
      </svg>
    </div>

    <svg class="back-button" width="48" height="28" viewBox="0 0 48 28" aria-label="Back">
      <path d="M46 14 H3 M15 2 L3 14 L15 26" stroke="var(--back-arrow)" stroke-width="2.5" fill="none" stroke-linecap="round" stroke-linejoin="round"/>
    </svg>

    <div class="score score-remaining"><span class="score-value">102</span><span class="score-label">REMAINING</span></div>
    <div class="score score-correct"><span class="score-value">24</span><span class="score-label">CORRECT</span></div>
    <div class="score score-wrong"><span class="score-value">4</span><span class="score-label">WRONG</span></div>
  </header>

  <h1 class="kanji" lang="ja">名</h1>
  <p class="reading" lang="ja">メイ, ミョウ. な</p>

  <section class="answer-grid" aria-label="Answer choices">
    <div class="answer">Seven</div>
    <div class="answer is-wrong">Person</div>
    <div class="answer">Long</div>
    <div class="answer is-correct">Name</div>
    <div class="answer">Come</div>
    <div class="answer">Many</div>
    <div class="answer">Write</div>
    <div class="answer">In</div>
    <div class="answer">Station</div>
  </section>

  <div class="action action-favorite">
    <svg width="30" height="29" viewBox="0 0 30 29" aria-hidden="true">
      <path d="M15 2 L18.8 10.4 L28 11.3 L21 17.4 L23.1 26.5 L15 21.7 L6.9 26.5 L9 17.4 L2 11.3 L11.2 10.4 Z" fill="none" stroke="var(--favorite-star)" stroke-width="1.8" stroke-linejoin="round"/>
    </svg>
    Add to Favorite
  </div>
  <div class="action action-skip">Skip Word</div>
</main>
</body>
</html>
```